Dental office needs flyer Design

We need a flier design for our Dental office based in Rockville MD. We provide premium dental care services including General and Ortho.

Flier Audience - Upper Middle Class, Individual professionals, Family, urban living,

Flier Focus - Promote "Grin Circle" program offered by the office
Key Highlights of the program - $69 for individual, $59 per person for family of two, $49 per person for a family 3, $39 per person for a family of 4. Design thoughts - Circle from big size to small with visual representation of individual and family size. The subscription is per month and annual membership, Also with the membership member will receive 15 - 25% of procedures. 3 - 4 cleanings a year, One XRay per year, One Emergency Exam per year, easy monthly payments, No Deductible, No yearly maximums, No Exclusions.

Flier Design considerations
Door Hanger, Eye Catchy shape,

Dental Office Highlights - No more than 9 patients a day so no double booking, no waiting; Before and after hours appointments, weekend appointments are available for emergencies, Direct access to Dentist,

Services Provided
1. Preventative Care
2. Orthodontics - Braces, Clearomet,
3. Cosmetic - Veneers, Teeth Whitening, Bonding
4. Bridges, Implants, Crown, Filling,
5. Dentures
6. Root Canal, Extractions, Gum Treatments

Location - 2836 Thornbury Ln Rockville MD 20853
PH: 301 555 0148
Website : www.DentistKalvo.com

Target Market(s)

Upper Middle Class, Individual professionals, Family, urban living,

Industry/Entity Type

Dental

Font styles to use
Decorative
Script

Requirements
Must have
• Promote "Grin Circle" program offered by the office
• Key Highlights of the program - $69 for individual, $59 per person for family of two, $49 per person for a family 3, $39 per person for a family of 4. Design thoughts - Circle from big size to small with visual representation of individual and family size. The subscription is per month and annual membership, Also with the membership member will receive 15 - 25% of procedures. 3 - 4 cleanings a year, One XRay per year, One Emergency Exam per year, easy monthly payments, No Deductible, No yearly maximums, No Exclusions.
• Location - 2836 Thornbury Ln Rockville MD 20853
• PH: 301 555 0148
• Website : www.DentistKalvo.com
Nice to have
• Eye Catchy Shape for Flier

```html
<!DOCTYPE html>
<html lang="en">
<head>
<meta charset="utf-8">
<title>Grin Circle Membership Flyer</title>
<link rel="stylesheet" href="https://fonts.googleapis.com/css2?family=Arvo:wght@700&family=Barlow+Condensed:wght@500;600&family=Open+Sans:wght@700&display=swap">
<style>
  :root {
    --page-bg: #ecebe8;
    --paper: #ffffff;
    --cyan: #29abe2;
    --cyan-light: #4fc3f0;
    --green: #6abf3f;
    --green-dark: #2e6b30;
    --green-mark: #2e7d3a;
    --navy: #263d8c;
    --price-blue: #1f4e8c;
    --photo-warm: #f1c9c4;
    --photo-pink: #f6dde6;
    --photo-cool: #dfe8ef;
  }
  html, body {
    margin: 0;
    width: 1200px;
    height: 1200px;
    overflow: hidden;
    background: var(--page-bg);
  }
  .flyer {
    position: absolute;
    left: 337px;
    top: 42px;
    width: 527px;
    height: 1116px;
    background: var(--paper);
    box-shadow: 0 2px 6px rgba(0,0,0,0.12);
  }
  .flyer svg { display: block; }
  .brand-mark { fill: var(--green-mark); }
  .brand-tagline {
    font-family: "Open Sans", sans-serif;
    font-weight: 700;
    font-size: 10.5px;
    fill: #1a1a1a;
  }
  .practice-name {
    font-family: "Arvo", serif;
    font-weight: 700;
    font-size: 29px;
    fill: var(--cyan);
  }
  .join-line {
    font-family: "Arvo", serif;
    font-weight: 700;
    font-size: 40px;
    fill: var(--green-mark);
  }
  .program-name {
    font-family: "Arvo", serif;
    font-weight: 700;
    font-size: 72px;
    fill: var(--cyan);
    stroke: #e9f7d9;
    stroke-width: 8px;
    paint-order: stroke;
    stroke-linejoin: round;
  }
  .offer-head {
    font-family: "Barlow Condensed", sans-serif;
    font-weight: 600;
    font-size: 31px;
    fill: #ffffff;
  }
  .offer-discount {
    font-family: "Barlow Condensed", sans-serif;
    font-weight: 600;
    font-size: 52px;
    fill: var(--green);
  }
  .benefit {
    font-family: "Barlow Condensed", sans-serif;
    font-weight: 500;
    font-size: 21px;
    fill: #ffffff;
  }
  .membership-type {
    font-family: "Barlow Condensed", sans-serif;
    font-weight: 600;
    font-size: 21px;
    fill: var(--green-dark);
    text-anchor: middle;
  }
  .price {
    font-family: "Barlow Condensed", sans-serif;
    font-weight: 600;
    font-size: 46px;
    fill: var(--price-blue);
    text-anchor: middle;
  }
  .price .unit { font-size: 26px; }
  .price .currency { font-size: 32px; }
  .plan-size {
    font-family: "Barlow Condensed", sans-serif;
    font-weight: 500;
    font-size: 25px;
    fill: var(--cyan);
    text-anchor: middle;
  }
  .contact {
    font-family: "Arvo", serif;
    font-weight: 700;
    fill: #ffffff;
    text-anchor: end;
  }
  .contact-address { font-size: 18.5px; }
  .contact-phone { font-size: 29px; }
  .contact-phone .label { font-size: 18px; }
  .contact-web { font-size: 17.5px; }
</style>
</head>
<body>
<div class="flyer">
  <svg width="527" height="1116" viewBox="0 0 527 1116" xmlns="http://www.w3.org/2000/svg">
    <defs>
      <linearGradient id="familyTone" x1="0" y1="0" x2="1" y2="1">
        <stop offset="0" stop-color="#e9d4cf"/>
        <stop offset="0.5" stop-color="#f1c9c4"/>
        <stop offset="1" stop-color="#f6dde6"/>
      </linearGradient>
      <linearGradient id="portraitTone" x1="0" y1="0" x2="0" y2="1">
        <stop offset="0" stop-color="#8a6a55"/>
        <stop offset="0.45" stop-color="#f0cfc2"/>
        <stop offset="1" stop-color="#eab9ae"/>
      </linearGradient>
      <clipPath id="flyerClip"><rect width="527" height="1116"/></clipPath>
    </defs>

    <g clip-path="url(#flyerClip)">
      <!-- brand block -->
      <g class="brand">
        <circle class="brand-mark" cx="93" cy="78" r="40"/>
        <text class="brand-tagline" x="93" y="140" text-anchor="middle">PARKWOOD DENTAL CARE</text>
        <text class="brand-tagline" x="93" y="155" text-anchor="middle">ROCKVILLE, MARYLAND</text>
      </g>
      <text class="practice-name" x="187" y="83">Smiles of</text>
      <text class="practice-name" x="187" y="116">Parkwood Hills</text>

      <!-- offer shapes -->
      <path fill="var(--green)" d="M0,185 C150,190 300,300 327,470 C340,560 335,610 330,660 L0,700 Z"/>
      <path fill="var(--navy)" d="M0,270 C150,280 290,380 315,520 C325,580 320,620 312,660 L0,720 Z"/>

      <!-- headline -->
      <text class="join-line" x="241" y="185">Join our</text>
      <text class="program-name" x="30" y="250">Grin Circle</text>

      <!-- offer copy -->
      <text class="offer-head" x="26" y="345">GET YOUR</text>
      <text class="offer-head" x="26" y="377">MEMBERSHIP</text>
      <text class="offer-head" x="26" y="409">&amp; RECEIVE</text>
      <text class="offer-discount" x="26" y="470">15-25% OFF</text>
      <text class="benefit" x="26" y="504">3 - 4 cleanings a year</text>
      <text class="benefit" x="26" y="530">One XRay per year</text>
      <text class="benefit" x="26" y="557">One Emergency Exam per year</text>
      <text class="benefit" x="26" y="583">Easy monthly payments</text>
      <text class="benefit" x="26" y="610">No Deductible</text>
      <text class="benefit" x="26" y="636">No yearly maximums</text>
      <text class="benefit" x="26" y="662">No Exclusions</text>

      <!-- pricing -->
      <text class="membership-type" x="414" y="278">MONTHLY OR ANNUAL</text>
      <text class="membership-type" x="414" y="303">MEMBERSHIP</text>

      <text class="price" x="414" y="350"><tspan class="currency">$</tspan>69<tspan class="unit">p/p</tspan></text>
      <text class="plan-size" x="414" y="377">individual</text>
      <text class="price" x="414" y="430"><tspan class="currency">$</tspan>59<tspan class="unit">p/p</tspan></text>
      <text class="plan-size" x="414" y="457">family of 2</text>
      <text class="price" x="414" y="510"><tspan class="currency">$</tspan>49<tspan class="unit">p/p</tspan></text>
      <text class="plan-size" x="414" y="537">family of 3</text>
      <text class="price" x="414" y="590"><tspan class="currency">$</tspan>39<tspan class="unit">p/p</tspan></text>
      <text class="plan-size" x="414" y="617">family of 4</text>

      <!-- photo area -->
      <path fill="url(#familyTone)" role="img" aria-label="Photo of a smiling young family: mother, father and baby"
            d="M0,720 C120,650 300,630 527,665 L527,994 L0,994 Z"/>
      <path fill="none" stroke="var(--cyan-light)" stroke-width="7"
            d="M0,722 C120,652 300,632 527,667"/>
      <circle cx="111" cy="806" r="112" fill="url(#portraitTone)" role="img" aria-label="Portrait photo of a smiling young woman"/>
      <circle cx="111" cy="806" r="112" fill="none" stroke="var(--cyan-light)" stroke-width="8"/>

      <!-- contact band -->
      <rect x="0" y="993" width="527" height="123" fill="var(--cyan-light)"/>
      <text class="contact contact-address" x="499" y="1034">2836 Thornbury Ln Rockville MD 20853</text>
      <text class="contact contact-phone" x="499" y="1066"><tspan class="label">Ph: </tspan>301 555 0148</text>
      <text class="contact contact-web" x="499" y="1093">www.DentistKalvo.com</text>
    </g>
  </svg>
</div>
</body>
</html>
```